Webdesign für Gerüstbau Wendrich
Zielgruppe
In der über 20-jährigen erfolgreichen Firmengeschichte ist die Firma Gerüstbau Wendrich GmbH ein leistungsstarker und kompetenter Partner für Kunden im Raum Sachsen und Thüringen. Der Aktionsradius erstreckt sich auf ca. 100 km um die Stadt Glauchau OT Niederschindmaas herum. Das Unternehmen arbeitet ausschließlich mit Kornath-Gerüsten.
Dafür stehen ca. 40.000 m² Kornath-Flink-Gerüst, ca. 4.000 m² Modulgerüst, Kassetten- und Planendächer, Treppenaufgänge und Nottreppen, Fahr- und Rollgerüste sowie weitere Sonderteile zur Verfügung.
Zielgruppe sind:
- Bau- und Dachdeckerfirmen,
- Handwerksbetriebe,
- Ingenieurbüros,
- Kommunen,
- Kirchen,
- landwirtschaftlichen Betriebe,
- Industrie
- und Privatpersonen
Aufgabenstellung
Unserem Auftraggeber gefällt ein großes Auftaktfoto gut, ansonsten ist er offen für ein modernes Layout.
- Layout als PSD
- Notwendige Bilder ausschließlich von Bildfundus.example
- Bitte nur die Startseite layouten
- blau des Logos und eine Zweitfarbe
- Slogan: Wir lösen Ihre Gerüstprobleme! Sprechen Sie mit uns!

```html
<!DOCTYPE html>
<html lang="de">
<head>
<meta charset="utf-8">
<title>Gerüstbau Wendrich – Startseite</title>
<link href="https://fonts.googleapis.com/css2?family=Roboto:wght@400;500;700&family=Poppins:wght@400&display=swap" rel="stylesheet">
<style>
:root{
  --blue:#1a5a94;
  --blue-dark:#155089;
  --green:#7ab832;
  --text:#555;
  --dark:#2b2b2b;
  --grey-bg:#f2f2f2;
  --white:#fff;
}
*{margin:0;padding:0;box-sizing:border-box}
html,body{width:1200px;height:2368px;overflow:hidden;background:var(--white);font-family:"Roboto",sans-serif;color:var(--text)}
.page{position:relative;width:1200px;height:2368px}
.header{position:absolute;top:0;left:0;width:1200px;height:100px}
.brand{position:absolute;left:235px;top:15px;display:flex;align-items:center;gap:14px}
.brand-mark{width:71px;height:71px;background:var(--blue)}
.brand-name{font-size:12px;font-weight:500;color:var(--blue);width:0;white-space:nowrap;position:absolute;left:84px;top:6px}
.brand-tagline{position:absolute;left:85px;top:20px;font-family:"Poppins",sans-serif;font-size:12px;line-height:16px;color:var(--blue);white-space:nowrap}
.nav{position:absolute;top:52px;left:505px;display:flex;font-size:10.5px;color:#444}
.nav span{margin-right:29px}
.nav .active{color:var(--green)}
.nav .has-sub::after{content:"";display:inline-block;width:4px;height:4px;border-right:1px solid #444;border-bottom:1px solid #444;transform:rotate(45deg);margin-left:6px;position:relative;top:-2px}
.contact-btn{position:absolute;left:879px;top:48px;width:86px;height:22px;border-radius:11px;background:var(--green);color:#fff;font-size:8px;font-weight:700;display:flex;align-items:center;padding-left:17px}
.contact-btn::after{content:"@";position:absolute;right:0;top:0;width:27px;height:22px;border-left:1px solid rgba(255,255,255,.6);display:flex;align-items:center;justify-content:center;font-size:12px}
.hero{position:absolute;top:100px;left:0;width:1200px;height:418px;background:linear-gradient(180deg,#8fb6df 0%,#c9dbee 35%,#b7b3a6 60%,#6f7d4f 100%)}
.hero-title{position:absolute;right:227px;top:145px;text-align:right}
.hero-title div{display:inline-block;background:rgba(34,34,34,.92);color:#fff;font-size:30px;padding:4px 16px 4px 20px;margin-bottom:4px}
.hero-title b{color:var(--green);font-weight:500}
.label{display:inline-block;position:relative;background:var(--green);color:#fff;font-weight:700;font-size:17px;padding:5px 12px}
.label::after{content:"";position:absolute;left:0;bottom:-6px;border-left:6px solid var(--green);border-bottom:6px solid transparent}
.label.center::after{left:50%;margin-left:-5px;border-left:5px solid transparent;border-right:5px solid transparent;border-top:6px solid var(--green);border-bottom:0}
.about{position:absolute;top:518px;left:0;width:1200px;height:333px}
.about .label{position:absolute;left:235px;top:50px}
.about p{position:absolute;left:235px;top:102px;width:345px;font-size:10px;line-height:18.7px}
.btn-outline{position:absolute;left:235px;top:259px;width:106px;height:31px;border:2px solid var(--blue);border-radius:16px;color:var(--blue);font-size:10px;font-weight:700;display:flex;align-items:center;justify-content:center}
.about-visual{position:absolute;left:600px;top:35px;width:390px;height:275px;background:radial-gradient(ellipse at 50% 85%,#e6e6e6 0%,#f6f6f6 45%,#fff 70%)}
.services{position:absolute;top:851px;left:0;width:1200px;height:689px;background:var(--grey-bg);text-align:center}
.services .label{margin-top:54px}
.services .intro{margin-top:18px;font-size:10px;line-height:18.7px}
.cards{position:absolute;left:235px;top:253px;display:flex;gap:19px}
.card{width:231px;background:#fff;box-shadow:0 1px 3px rgba(0,0,0,.08)}
.card .photo{height:251px}
.card h3{height:57px;display:flex;align-items:center;justify-content:center;font-size:12px;font-weight:500;color:#333}
.arrow{position:absolute;top:370px;width:14px;height:28px}
.dots{position:absolute;top:607px;left:0;width:1200px;display:flex;justify-content:center;gap:6px}
.dots i{width:5px;height:5px;border-radius:50%;background:var(--green)}
.dots i:first-child{width:7px;height:7px;margin-top:-1px;background:var(--blue)}
.news{position:absolute;top:1540px;left:0;width:1200px;height:520px;text-align:center}
.news .label{margin-top:56px}
.news-cards{position:absolute;left:234px;top:123px;display:flex;gap:19px;text-align:left}
.news-card{width:232px;height:325px;background:#fff;box-shadow:0 1px 4px rgba(0,0,0,.12);position:relative}
.news-card .photo{height:135px}
.news-card h3{margin:28px 17px 0;font-size:12px;line-height:15px;font-weight:500;color:var(--dark)}
.news-card p{margin:16px 17px 0;font-size:9.2px;line-height:15.6px}
.news-card a{position:absolute;left:17px;top:295px;font-size:9.5px;font-weight:700;color:var(--blue);text-decoration:none}
.band{position:absolute;top:2060px;left:0;width:1200px;height:30px}
.footer{position:absolute;top:2090px;left:0;width:1200px;height:230px;background:var(--blue);color:#fff}
.footer h4{position:absolute;top:48px;font-size:11.5px;font-weight:700}
.footer ul{position:absolute;top:80px;list-style:none;font-size:8.5px;line-height:25.7px}
.footer li::before{content:"";display:inline-block;width:4px;height:4px;border-radius:50%;background:#fff;margin-right:9px;vertical-align:middle}
.contact-row{position:absolute;left:528px;display:flex;gap:9px;font-size:8.5px;line-height:16px}
.contact-row svg{flex:none;margin-top:3px}
.phone{font-size:11px;font-weight:700}
.partner{position:absolute;left:747px;top:48px}
.partner .name{font-size:20px;font-weight:400;display:flex;align-items:center;gap:8px}
.partner .name i{width:16px;height:16px;background:#fff;display:inline-block}
.partner small{display:block;font-size:8.5px;margin-top:10px}
.partner .legal{font-size:8.5px;margin-top:14px}
.social{display:flex;gap:9px;margin-top:14px}
.social i{width:16px;height:16px;border-radius:50%;background:#fff;display:block}
.bottom{position:absolute;top:2320px;left:0;width:1200px;height:48px;font-size:8.5px;color:#777}
.badge{position:absolute;left:235px;top:9px;width:26px;height:26px;background:#7ea8d1}
.bottom .reg{position:absolute;left:273px;top:18px}
.bottom .copy{position:absolute;right:234px;top:18px}
</style>
</head>
<body>
<div class="page">

<header class="header">
  <div class="brand">
    <div class="brand-mark"></div>
  </div>
  <div class="brand-tagline" style="left:320px;top:35px">Wir lösen auch<br>Ihre Gerüstprobleme!</div>
  <div style="position:absolute;left:246px;top:44px;width:50px;text-align:center;color:#fff;font-size:6.5px;font-weight:500;line-height:8px">Gerüstbau<br>Wendrich</div>
  <nav class="nav">
    <span class="active">Startseite</span>
    <span class="has-sub" style="margin-left:1px">Leistungen</span>
    <span style="margin-left:-10px">Unternehmen</span>
    <span>Aktuelles</span>
    <span>Karriere</span>
  </nav>
  <div class="contact-btn">Kontakt</div>
</header>

<section class="hero" role="img" aria-label="Foto: eingerüstetes historisches Schloss mit Kirchturm unter blauem Himmel">
  <div class="hero-title">
    <div>ÜBER <b>30 JAHRE</b></div><br>
    <div>GERÜSTBAU WENDRICH</div>
  </div>
</section>

<section class="about">
  <h2 class="label">ÜBER UNS</h2>
  <p>In der über 20-jährigen erfolgreichen Firmengeschichte waren und sind wir stets ein leistungsstarker und kompetenter Partner für unsere Kunden im Raum Sachsen und Thüringen. Unser Aktionsradius erstreckt sich auf ca. 100 km im Umkreis. Mit unserem im Jahresdurchschnitt 15-köpfigem Team sind wir in der Lage, die meisten im Gerüstbau geforderten Leistungen zu erbringen. Einen Einblick über von uns ausgeführte Arbeiten erhalten Sie auf der nachfolgenden Seite.</p>
  <div class="btn-outline">Referenzen</div>
  <div class="about-visual" role="img" aria-label="Freigestelltes Baugerüst mit Werbebanner"></div>
</section>

<section class="services">
  <h2 class="label center">UNSERE LEISTUNGEN</h2>
  <p class="intro">Wir arbeiten ausschließlich mit Kornath-Gerüsten.<br>Dafür stehen uns ca. 40.000 m² Kornath-Flink-Gerüst, ca. 4.000 m² Modulgerüst, Kassetten- und Planendächer,<br>Treppenaufgänge und Nottreppen, Fahr- und Rollgerüste sowie weitere Sonderteile zur Verfügung.<br><br>Für den Transport des Gerüstmaterials haben wir vier LKW, z.T. mit Ladekran, und einen<br>Transporter im Einsatz.</p>
  <svg class="arrow" style="left:178px" viewBox="0 0 14 28"><path d="M12 2 2 14l10 12" fill="none" stroke="#bbb" stroke-width="4"/></svg>
  <svg class="arrow" style="left:1000px" viewBox="0 0 14 28"><path d="M2 2l10 12L2 26" fill="none" stroke="#aaa" stroke-width="4"/></svg>
  <div class="cards">
    <div class="card"><div class="photo" role="img" aria-label="Foto: eingerüstete Altbaufassade" style="background:linear-gradient(180deg,#d9dce0,#6f6a62)"></div><h3>FASSADENGERÜSTE</h3></div>
    <div class="card"><div class="photo" role="img" aria-label="Foto: Gebäude mit Kassettendach und Planen" style="background:linear-gradient(180deg,#7fa3d6,#e4e6ea 55%,#6e7f50)"></div><h3>KASSETTENDÄCHER</h3></div>
    <div class="card"><div class="photo" role="img" aria-label="Foto: Raumgerüst in einer Halle" style="background:linear-gradient(180deg,#5a6f80,#a5704c 50%,#4b4f52)"></div><h3>RAUMGERÜSTE</h3></div>
  </div>
  <div class="dots"><i></i><i></i><i></i></div>
</section>

<section class="news">
  <h2 class="label center" style="padding:5px 14px">AKTUELLES</h2>
  <div class="news-cards">
    <article class="news-card">
      <div class="photo" role="img" aria-label="Foto: Gerüst an Schlossmauer" style="background:linear-gradient(160deg,#a9c3e0,#9a8774 70%,#6b5443)"></div>
      <h3>Schloss Lichtenstein in Sachsen -<br>Wir bauen das Gerüst!</h3>
      <p>Das Schloss Lichtenstein befindet sich in exponierter Lage auf dem Schlossberg in Lichtenstein und wird derzeit denkmal-schutzgerecht zu einem Schlosshotel mit Wellnesslandschaft umgebaut und saniert.</p>
      <a href="#">mehr erfahren</a>
    </article>
    <article class="news-card">
      <div class="photo" role="img" aria-label="Foto: Handwerker mit gelbem Schutzhelm und Werkzeuggürtel" style="background:linear-gradient(135deg,#8a5a3c,#c9a03a 45%,#a67a4a)"></div>
      <h3>Neue engagierte Mitarbeiter<br>für das Jahr 2022 gesucht</h3>
      <p>Sie sind Gerüstbauer oder haben einen an-deren einschlägigen Bauberuf und möchten sich beruflich verändern? Dann rufen Sie bei uns an!&nbsp; Auch Gerüstbauhelfer sind herzlich willkommen, Sie werden hier angelernt.</p>
      <a href="#">mehr erfahren</a>
    </article>
    <article class="news-card">
      <div class="photo" role="img" aria-label="Foto: eingerüstetes Haus am Marktplatz" style="background:linear-gradient(160deg,#6d8fc8,#c7b48a 50%,#9d9d9d)"></div>
      <h3>Unser letztes Projekt:<br>Auf dem Zwickauer Hauptmarkt</h3>
      <p>Lorem ipsum dolor sit amet, consetetur sadipscing elitr, sed diam nonumy eirmod tempor invidunt ut labore et dolore magna aliquyam erat, sed diam voluptua. At vero eos et accusam et justo duo dolores et...</p>
      <a href="#">mehr erfahren</a>
    </article>
  </div>
</section>

<svg class="band" viewBox="0 0 1200 30" preserveAspectRatio="none" aria-hidden="true">
  <line x1="0" y1="10" x2="1200" y2="10" stroke="#eee" stroke-width="2"/>
  <line x1="0" y1="24" x2="1200" y2="24" stroke="#eee" stroke-width="2"/>
</svg>

<footer class="footer">
  <h4 style="left:234px">UNSERE GERÜSTE</h4>
  <ul style="left:240px"><li>Fassadengerüste</li><li>Kassettendächer</li><li>Spezialgerüste</li><li>Treppentürme</li></ul>
  <ul style="left:346px"><li>für Kirchen &amp; Denkmälern</li><li>Fahrgerüste</li><li>Über uns</li><li>Karriere</li></ul>
  <h4 style="left:528px">KONTAKT</h4>
  <div class="contact-row" style="top:83px">
    <svg width="11" height="11" viewBox="0 0 12 12"><rect width="12" height="12" rx="2" fill="#fff"/><path d="M3.5 2.5l1.5 2-1 1c.5 1 1.5 2 2.5 2.5l1-1 2 1.5-.8 1.2C6 9.5 2.5 6 2.3 3.3z" fill="var(--blue)"/></svg>
    <span class="phone">03761-555210</span>
  </div>
  <div class="contact-row" style="top:109px">
    <svg width="11" height="10" viewBox="0 0 12 10"><path d="M6 0 0 5h1.5v5h3.5V7h2v3h3.5V5H12z" fill="#fff"/></svg>
    <span>Lindenweg 4<br>08390 Musterdorf</span>
  </div>
  <div class="contact-row" style="top:148px">
    <svg width="10" height="10" viewBox="0 0 10 10"><circle cx="5" cy="5" r="4" fill="none" stroke="#fff" stroke-width="1.4"/><path d="M5 2.5V5h2" fill="none" stroke="#fff" stroke-width="1.2"/></svg>
    <span>Öffnungszeiten: 8:00 - 17:00 Uhr<br>Samstag von 8:00 - 14:0 Uhr</span>
  </div>
  <div class="partner">
    <div class="name">Kornath <i></i></div>
    <small>Wir bauen mir dem Kornath Gerüst-System</small>
    <div class="legal">Datenschutz | Impressum</div>
    <div class="social"><i></i><i></i><i></i></div>
  </div>
</footer>

<div class="bottom">
  <div class="badge"></div>
  <span class="reg">Die Präqualifizierung erfolgte unter der Registriernummer 110.004271</span>
  <span class="copy">© 2022 Gerüstbau Wendrich GmbH</span>
</div>

</div>
</body>
</html>
```